Vormace

I need a professional web site that is directed at the energy industry, Oil, Gas, Mining
I need the website to have the usual pages
1. home page
2. news page.
3. contact us page
4. About us
and a CMS admin section to add further pages and content
Must be Google friendly with SEO facility

Target Market(s)

energy industry, Oil, Gas, Mining

Industry/Entity Type

Industry

Font styles to use
Sans Serif

Colors
faa54b
85cae6
cadf82

Requirements
Must have
• social media icons
site map

```html
<!DOCTYPE html>
<html lang="en">
<head>
<meta charset="utf-8">
<title>Vormace – Energy, Oil, Gas & Mining</title>
<link href="https://fonts.googleapis.com/css2?family=Open+Sans:wght@400;600;700&display=swap" rel="stylesheet">
<style>
:root{
  --orange:#faa54b;
  --blue:#85cae6;
  --green:#cadf82;
  --white:#ffffff;
  --ink:#222222;
  --muted:#7a7a7a;
  --rule:#e6e6e6;
}
*{box-sizing:border-box;margin:0;padding:0}
html,body{width:1168px;height:1200px;overflow:hidden;background:var(--white)}
body{font-family:"Open Sans",Arial,sans-serif;color:var(--ink);position:relative}
.hero{position:absolute;left:0;top:0;width:1168px;height:604px;
  background:linear-gradient(160deg,#1d4f8a 0%,#3d6aa0 22%,#c9744a 45%,#f0a040 65%,#f7c45a 80%,#e8923a 100%)}
.slider-dots{position:absolute;left:552px;top:575px;display:flex;gap:6px}
.slider-dots span{width:12px;height:12px;border:1.5px solid var(--white);border-radius:50%}
.slider-dots span.active{border-color:#555}
.site-header{position:absolute;left:157px;top:0;width:854px;height:103px;background:var(--white)}
.brand{position:absolute;left:28px;top:38px;display:flex;align-items:center;gap:8px;
  font-weight:700;font-size:24px;letter-spacing:1px;color:var(--ink)}
.brand i{width:12px;height:12px;border-radius:50%;background:var(--orange);display:block}
.main-nav{position:absolute;left:371px;top:0;height:103px;display:flex}
.main-nav a{display:flex;align-items:center;height:103px;padding:0 22px;font-size:14px;color:var(--ink);text-decoration:none}
.main-nav a.current{background:var(--orange);color:var(--white);padding:0 26px}
.provide{position:absolute;left:0;top:604px;width:1168px;height:377px;background:var(--green)}
.provide h2{position:absolute;top:28px;width:100%;text-align:center;color:var(--white);font-weight:400;font-size:26px}
.card{position:absolute;top:81px;width:192px}
.card .photo{height:151px}
.card .label{height:48px;background:var(--blue);display:flex;align-items:center;justify-content:space-between;padding:0 9px 0 16px;font-size:13px;color:#2a3a44;text-transform:uppercase}
.card .label svg{width:23px;height:23px}
.card p{margin-top:10px;font-size:9.5px;line-height:16px;color:var(--white)}
.site-footer{position:absolute;left:0;top:981px;width:1168px;height:172px}
.col{position:absolute;top:18px;list-style:none;font-size:10.5px}
.col li{height:25px}
.social{position:absolute;left:810px;top:18px;list-style:none;font-size:10.5px}
.social li{height:44px;display:flex;align-items:flex-start;width:110px;justify-content:space-between}
.social i{width:14px;height:14px;border-radius:50%;background:var(--muted);display:block}
.legal{position:absolute;left:0;top:1153px;width:1168px;border-top:1px solid var(--rule);text-align:center;padding-top:18px;font-size:10.5px}
</style>
</head>
<body>
<section class="hero" role="img" aria-label="Electricity pylon silhouetted against a sunset sky">
  <div class="slider-dots"><span class="active"></span><span></span><span></span><span></span></div>
</section>

<header class="site-header">
  <div class="brand"><i></i>VORMACE</div>
  <nav class="main-nav">
    <a class="current" href="#">Home</a>
    <a href="#">About us</a>
    <a href="#">Industries</a>
    <a href="#">News</a>
    <a href="#">Contact us</a>
  </nav>
</header>

<main class="provide">
  <h2>WHAT WE PROVIDE</h2>
  <article class="card" style="left:168px">
    <div class="photo" role="img" aria-label="Technician installing solar panels on a roof" style="background:linear-gradient(180deg,#5d7ec4,#2c4a8e 60%,#3a5fa8)"></div>
    <div class="label">Energy Industry<svg viewBox="0 0 24 24"><circle cx="12" cy="12" r="10" fill="none" stroke="#fff" stroke-width="2.4"/><path d="M7 12h8M12 8l4 4-4 4" fill="none" stroke="#fff" stroke-width="2.4"/></svg></div>
    <p>Lorem Ipsum is simply dummy text of the printing and typesetting industry. Lorem Ipsum has been the industry's</p>
  </article>
  <article class="card" style="left:382px">
    <div class="photo" role="img" aria-label="Offshore oil platform at sea" style="background:linear-gradient(180deg,#cfc9c2,#8c8f96 55%,#1e2a3e)"></div>
    <div class="label">Oil<svg viewBox="0 0 24 24"><circle cx="12" cy="12" r="10" fill="none" stroke="#fff" stroke-width="2.4"/><path d="M7 12h8M12 8l4 4-4 4" fill="none" stroke="#fff" stroke-width="2.4"/></svg></div>
    <p>Lorem Ipsum is simply dummy text of the printing and typesetting industry. Lorem Ipsum has been the industry's</p>
  </article>
  <article class="card" style="left:596px">
    <div class="photo" role="img" aria-label="Gas rig lit up at dusk over water" style="background:linear-gradient(180deg,#3c6ec2,#2a3d6a 55%,#b05a22 80%,#1a2030)"></div>
    <div class="label">Gas<svg viewBox="0 0 24 24"><circle cx="12" cy="12" r="10" fill="none" stroke="#fff" stroke-width="2.4"/><path d="M7 12h8M12 8l4 4-4 4" fill="none" stroke="#fff" stroke-width="2.4"/></svg></div>
    <p>Lorem Ipsum is simply dummy text of the printing and typesetting industry. Lorem Ipsum has been the industry's</p>
  </article>
  <article class="card" style="left:809px">
    <div class="photo" role="img" aria-label="Yellow mining dump truck and excavator" style="background:linear-gradient(180deg,#4a7ac8,#9aa3a6 50%,#c8a030 70%,#5a4c3a)"></div>
    <div class="label">Mining<svg viewBox="0 0 24 24"><circle cx="12" cy="12" r="10" fill="none" stroke="#fff" stroke-width="2.4"/><path d="M7 12h8M12 8l4 4-4 4" fill="none" stroke="#fff" stroke-width="2.4"/></svg></div>
    <p>Lorem Ipsum is simply dummy text of the printing and typesetting industry. Lorem Ipsum has been the industry's</p>
  </article>
</main>

<footer class="site-footer">
  <ul class="col" style="left:183px"><li>Home</li><li>About us</li><li>Industries</li><li>News</li><li>Contact us</li></ul>
  <ul class="col" style="left:345px"><li>Energy Industry</li><li>Oil</li><li>Gas</li><li>Mining</li></ul>
  <ul class="col" style="left:519px"><li>Nordfeld Büro</li><li>Lindenweg 42b</li><li>10117 Berlin</li><li>Germany</li><li>Telephone: +49 30 55501234</li><li>E-mail: hello@vormace-mail.de</li></ul>
  <ul class="social"><li>Friendlane<i></i></li><li>Chirpline<i></i></li><li>Workhub<i></i></li></ul>
</footer>

<div class="legal">© 2014 Company Name ,All Right Reserved</div>
</body>
</html>
```